Restaurant Bar website in Oakland

Landing page that looks good on mobile and home. Easy to make changes to SEO and Menu page .
Might link with online ordering through the point of sale provider or not. Either way we want to be able to upload menus.
No forms need. Just landing page, about page with a paragraph and a few photos, address, hours and a mailto info@
A press page and an faq

Target Market(s)

Customers

Coding

Coded - Design and coding required

Number of Pages Required

4 page

Colors
00a990
ffc214

Requirements
Must have
• Simple to scroll
SEO
Simple to add menus
Our logo

```html
<!DOCTYPE html>
<html lang="en">
<head>
<meta charset="utf-8">
<title>Quenby's — Restaurant &amp; Bar</title>
<link rel="stylesheet" href="https://fonts.googleapis.com/css2?family=Open+Sans:wght@700&family=Montserrat:wght@400;700&display=swap">
<style>
  :root {
    --toolbar-dark: #1f2327;
    --header-green: #2d5237;
    --gold: #d4a04a;
    --hero-dark: #2a2622;
    --hero-mid: #4f463d;
    --hero-light: #6e665c;
    --napkin: #57514b;
    --body-text: #d8d0c6;
    --search-grey: #5f7a66;
  }
  * { margin: 0; padding: 0; box-sizing: border-box; }
  html, body {
    width: 1200px;
    height: 582px;
    overflow: hidden;
    background: var(--hero-dark);
  }
  .page {
    position: relative;
    width: 1200px;
    height: 582px;
    overflow: hidden;
  }
  .toolbar {
    position: absolute;
    top: 0; left: 0;
    width: 1200px;
    height: 28px;
    background: var(--toolbar-dark);
  }
  .site-header {
    position: absolute;
    top: 28px; left: 0;
    width: 1200px;
    height: 72px;
    background: var(--header-green);
    z-index: 2;
  }
  .brand {
    position: absolute;
    left: 129px;
    top: 0;
    height: 72px;
    display: flex;
    align-items: center;
    font-family: "Open Sans", sans-serif;
    font-weight: 700;
    font-size: 17px;
    color: var(--gold);
    text-decoration: none;
  }
  .main-nav {
    position: absolute;
    left: 744px;
    top: 0;
    height: 72px;
    display: flex;
    align-items: center;
    gap: 22px;
  }
  .main-nav a {
    font-family: "Open Sans", sans-serif;
    font-weight: 700;
    font-size: 12.5px;
    color: var(--gold);
    text-decoration: none;
    letter-spacing: 0.2px;
  }
  .search-toggle {
    position: absolute;
    left: 1064px;
    top: 28px;
  }
  .hero {
    position: absolute;
    top: 100px; left: 0;
    width: 1200px;
    height: 482px;
  }
  .hero-photo {
    position: absolute;
    inset: 0;
    background:
      radial-gradient(ellipse 340px 340px at 598px 256px, var(--hero-light) 0%, var(--hero-mid) 60%, transparent 82%),
      radial-gradient(ellipse 260px 320px at 1000px 240px, var(--napkin) 0%, transparent 80%),
      linear-gradient(100deg, #3a2e26 0%, var(--hero-dark) 30%, #3d3833 70%, #3a3531 100%);
  }
  .hero-title {
    position: absolute;
    top: 146px;
    left: 0;
    width: 1200px;
    text-align: center;
    font-family: "Montserrat", sans-serif;
    font-weight: 700;
    font-size: 96px;
    line-height: 120px;
    letter-spacing: 5px;
    color: var(--gold);
    text-transform: uppercase;
  }
  .hero-intro {
    position: absolute;
    top: 400px;
    left: 255px;
    width: 690px;
    font-family: "Montserrat", sans-serif;
    font-weight: 400;
    font-size: 16px;
    line-height: 29px;
    color: var(--body-text);
    text-align: center;
  }
</style>
</head>
<body>
  <div class="page">
    <div class="toolbar"></div>

    <header class="site-header">
      <a class="brand" href="#">Quenby's</a>
      <nav class="main-nav">
        <a href="#">HOME</a>
        <a href="#">ABOUT</a>
        <a href="#">OUR MENU</a>
        <a href="#">FAQ</a>
        <a href="#">PRESS</a>
      </nav>
      <svg class="search-toggle" width="16" height="16" viewBox="0 0 16 16" fill="none" stroke="var(--search-grey)" stroke-width="1.4" aria-label="Search">
        <circle cx="9.5" cy="6.5" r="5"/>
        <line x1="6" y1="10" x2="1.5" y2="14.5"/>
      </svg>
    </header>

    <section class="hero">
      <div class="hero-photo" role="img" aria-label="Overhead photo of a bowl of mashed potatoes with greens and bacon beside a spoon and linen napkin on a dark wooden table"></div>
      <h1 class="hero-title">Quenby's</h1>
      <p class="hero-intro">Sed ut perspiciatis unde omnis iste natus error sit voluptatem accusantium doloremque laudantium, totam rem aperiam, eaque ipsa quae ab illo inventore veritatis et quasi architectoeaque ipsa quae ab illo inventore.</p>
    </section>
  </div>
</body>
</html>
```